Guaranteed Job - Sleek Sexy Business Card UV Spot

Im looking for a sleek and sexy business card, that resembles elite or VIP status status.
our business is corinvale.example
you can view our products on there, but our main audience for handing out our cards will be for people in the hospitality industry, so it will need to impress high management and CEO of hotels and restaurants, bars, clubs etc...
the card features will have UV spot on both sides, 400gsm stock. standard size.
Artwork should be 86 x 54mm + 2mm bleed = 90 x 58mm
it should have a nice "unique" uv spot pattern that highlights the card, not a repeated pattern, theres no originality there, and it will be disregarded.
The written material will be:
Corin Vale Hospitality College (logo)
Tobin Marsh
Director
Phone: 1300 615 737
Mobile: 0455 817 296
Email: info@corinvale.example
website: www.corinvale.example
I'm looking for originality here, i don't want just a simple stock card, want something that has a wow factor for people.
You will find the logo attached. you may invert the white to black words to suit the background as you please.
thank you and good luck
As a side note, ive received a lot of proposals, im too busy to give feedback to each and every one, so if i havent provided feedback for your design within 24 hours, then consider it not acceptable, and you could resubmit another design.
So far i have not seen any design that stood out for me, they all seem pretty generic. there nothing thats unique, i would figure for the amount that im offering, that people would put some more effort and creativity into the design.
so far over 200 designs submitted, and nothing i have seen looks very original, everything looks like a different variation of the same stuff, i said it very clearly i wanted something unique, the only thing that has come close to it so far is this one
Reason: Ive received alot of design concepts and i have reviewed everyone, but i havent had time to give feedback to every single one, only the ones that have interested me, if i havent responded, its because i havent found it good enough.
so far only a few design have been on par with what ive been looking for, an attractive eye popping design.
heres a few of them,
http://files.pixelbazaar.example/design_img/51736/62418/62418_2840915_51736_image.jpg
http://files.pixelbazaar.example/design_img/51736/68254/68254_2841377_51736_image.jpg
theyre, both unique and original, and eye catching, the only thing theyre missing is the sexyness.
if you still think you have some creativity left in your minds, then throw it on here.
Reason: Sorry guys for the delay, I was in a serious accident and out of commission for the past few months, I'm just slowly recovering now, please bare with me as i try to attend to this project, it may take me awhile as I have other projects that are on standby, I'm not 100% at the moment, so im extending the deadline for 2 weeks right now. Thanks for your patience.
Hospitality

```html
<!DOCTYPE html>
<html lang="en">
<head>
<meta charset="utf-8">
<title>Corin Vale Hospitality College – Business Card</title>
<link href="https://fonts.googleapis.com/css2?family=Barlow:wght@500&family=Barlow+Condensed:wght@400;500&display=swap" rel="stylesheet">
<style>
  :root {
    --page-bg: #ffffff;
    --card-base: #aebfbe;
    --edge-blue: #6fd0f5;
    --strip-dark: #a2a4a6;
    --strip-light: #ffffff;
    --logo-white: #ffffff;
    --logo-silver: #e6eaea;
    --spot-faint-1: #bcc8c8;
    --spot-faint-2: #c9d2d2;
    --spot-mid: #e3e8e8;
    --spot-bright: #ffffff;
  }
  html, body {
    margin: 0;
    padding: 0;
    width: 1200px;
    height: 1000px;
    overflow: hidden;
    background: var(--page-bg);
  }
  .canvas {
    position: relative;
    width: 1200px;
    height: 1000px;
  }
  .card {
    position: absolute;
    top: 331px;
    width: 527px;
    height: 338px;
  }
  .card--front { left: 45px; }
  .card--back { left: 617px; }
  .card__surface {
    position: absolute;
    inset: 0;
    width: 527px;
    height: 338px;
    display: block;
  }
  .brand {
    position: absolute;
    left: 30px;
    top: 40px;
    display: flex;
    align-items: center;
    gap: 14px;
  }
  .brand__mark {
    width: 54px;
    height: 54px;
    background: var(--edge-blue);
  }
  .brand__name {
    font-family: "Barlow", sans-serif;
    font-weight: 500;
    color: var(--logo-white);
    line-height: 1;
    text-transform: uppercase;
  }
  .card--back .brand__name { color: var(--logo-silver); }
  .brand__title {
    display: block;
    font-size: 27px;
    letter-spacing: 0.5px;
  }
  .brand__sub {
    display: block;
    font-size: 12.5px;
    letter-spacing: 0.8px;
    margin-top: 5px;
  }
  .contact {
    position: absolute;
    left: 44px;
    top: 170px;
    margin: 0;
    padding: 0;
    list-style: none;
    font-family: "Barlow Condensed", sans-serif;
    font-weight: 500;
    font-size: 16px;
    letter-spacing: 0.6px;
    line-height: 22.6px;
    text-transform: uppercase;
  }
  .contact__line--org { color: var(--spot-faint-1); }
  .contact__line--person { color: var(--spot-faint-2); }
  .contact__line--phone { color: var(--spot-mid); }
  .contact__line--mobile { color: #eef1f1; }
  .contact__line--email,
  .contact__line--web { color: var(--spot-bright); }
</style>
</head>
<body>
<main class="canvas">

  <svg width="0" height="0" aria-hidden="true" style="position:absolute">
    <defs>
      <linearGradient id="strip-gradient" x1="0" y1="0" x2="0" y2="1">
        <stop offset="0" stop-color="#a2a4a6"/>
        <stop offset="1" stop-color="#ffffff"/>
      </linearGradient>
    </defs>
  </svg>

  <section class="card card--front" aria-label="Card front">
    <svg class="card__surface" viewBox="0 0 527 338" aria-hidden="true">
      <rect width="527" height="338" fill="url(#strip-gradient)"/>
      <polygon points="0,0 410,0 457,20 470,338 0,338" fill="var(--card-base)"/>
      <polyline points="410,0 457,20 470,338" fill="none" stroke="var(--edge-blue)" stroke-width="1.5"/>
    </svg>
    <div class="brand">
      <span class="brand__mark" aria-hidden="true"></span>
      <span class="brand__name">
        <span class="brand__title">Corin Vale</span>
        <span class="brand__sub">Hospitality College</span>
      </span>
    </div>
  </section>

  <section class="card card--back" aria-label="Card back">
    <svg class="card__surface" viewBox="0 0 527 338" aria-hidden="true">
      <rect width="527" height="338" fill="url(#strip-gradient)"/>
      <polygon points="0,0 410,0 457,20 470,338 0,338" fill="var(--card-base)"/>
      <polyline points="410,0 457,20 470,338" fill="none" stroke="var(--edge-blue)" stroke-width="1.5"/>
    </svg>
    <div class="brand">
      <span class="brand__mark" aria-hidden="true"></span>
      <span class="brand__name">
        <span class="brand__title">Corin Vale</span>
        <span class="brand__sub">Hospitality College</span>
      </span>
    </div>
    <ul class="contact">
      <li class="contact__line contact__line--org">Corin Vale Hospitality College</li>
      <li class="contact__line contact__line--person">Tobin Marsh (Director)</li>
      <li class="contact__line contact__line--phone">Phone: 1300 615 737</li>
      <li class="contact__line contact__line--mobile">Mobile: 0455 817 296</li>
      <li class="contact__line contact__line--email">Email: info@corinvale.example</li>
      <li class="contact__line contact__line--web">Website: www.corinvale.example</li>
    </ul>
  </section>

</main>
</body>
</html>
```